Hi Marlene,

I need your help to design another poster for Corporate & Private Catering.

Price List is as follow :

PACK 1: $15 per person (Min 10 people) This includes:
- 10 x Noodle Salads / Pho (All options included)
- 10 x Fresh Ricepaper Rolls
- 10 x Spring Rolls

PACK 1: $20 per person (Min 10 people) This includes:
- 10 x Rice (All options included)
- 10 x Spring Rolls

SPRING ROLLS (Seafood / Vegetarian)
20 Rolls = $30
30 Rolls = $45
40 Rolls = $60
50 Rolls = $75

FRESH RICEPAPER ROLLS
20 Rolls = $50
30 Rolls = $75
40 Rolls = $100
50 Rolls = $125

FRIED RICE (All options included)
- $50 per tray. Serve 5-7 people.

```html
<!DOCTYPE html>
<html lang="en">
<head>
<meta charset="utf-8">
<title>Catering Menu Flyer</title>
<link rel="stylesheet" href="https://fonts.googleapis.com/css2?family=Bebas+Neue&family=Montserrat:wght@400;700&display=swap">
<style>
  :root {
    --page-bg: #efe6d6;
    --flyer-bg: #1d1e21;
    --photo-tone: #34363d;
    --orange: #ec942f;
    --yellow: #f4d11b;
    --white: #ffffff;
    --grey: #8c8d90;
    --black: #0d0d0d;
  }
  * { box-sizing: border-box; margin: 0; padding: 0; }
  html, body { width: 1200px; height: 1180px; overflow: hidden; background: var(--page-bg); }
  .canvas { position: relative; width: 1200px; height: 1180px; }
  .flyer {
    position: absolute; left: 197px; top: 20px;
    width: 890px; height: 1258px;
    transform: scale(0.906); transform-origin: top left;
    background: var(--flyer-bg); overflow: hidden;
    box-shadow: 0 6px 18px rgba(0,0,0,.25);
  }
  .flyer-art { position: absolute; inset: 0; }
  .badge-title {
    position: absolute; left: 414px; top: 436px; width: 240px;
    font-family: "Bebas Neue", sans-serif; font-weight: 400; text-align: center; line-height: .9;
  }
  .badge-title .kicker { display: block; color: var(--yellow); font-size: 56px; }
  .badge-title .main { display: block; color: var(--white); font-size: 96px; }
  .menu-block { position: absolute; }
  .pack-label { font-family: "Bebas Neue", sans-serif; font-weight: 400; color: var(--grey); font-size: 46px; line-height: 1; margin-bottom: 2px; }
  .section-head { font-family: "Bebas Neue", sans-serif; font-weight: 400; color: var(--orange); font-size: 27px; line-height: 1.1; margin-bottom: 4px; white-space: nowrap; }
  .items { list-style: none; font-family: "Montserrat", sans-serif; color: var(--white); font-size: 18px; line-height: 24px; white-space: nowrap; }
  .items li::before { content: "\00BB"; color: var(--orange); font-weight: 700; margin-right: 6px; }
  .items strong { font-weight: 700; }
  .pack-one { left: 42px; top: 706px; }
  .pack-two { left: 42px; top: 886px; }
  .fried-rice { left: 40px; top: 1060px; }
  .spring-rolls { left: 512px; top: 757px; }
  .ricepaper-rolls { left: 512px; top: 937px; }
  .call-line {
    position: absolute; left: 42px; top: 1200px;
    font-family: "Bebas Neue", sans-serif; font-size: 42px; color: var(--black);
    display: flex; align-items: center; gap: 12px;
  }
  .call-line svg { width: 36px; height: 36px; }
</style>
</head>
<body>
<div class="canvas">
  <div class="flyer">
    <svg class="flyer-art" viewBox="0 0 890 1258" xmlns="http://www.w3.org/2000/svg">
      <defs>
        <radialGradient id="photoTone" cx="40%" cy="35%" r="70%">
          <stop offset="0" stop-color="#3d3f47"/>
          <stop offset="1" stop-color="#2a2b31"/>
        </radialGradient>
        <radialGradient id="soupTone" cx="50%" cy="50%" r="50%">
          <stop offset="0" stop-color="#8a6a4e"/>
          <stop offset="1" stop-color="#5a3e2a"/>
        </radialGradient>
        <radialGradient id="noodleTone" cx="50%" cy="50%" r="50%">
          <stop offset="0" stop-color="#e2c79a"/>
          <stop offset="1" stop-color="#b8924f"/>
        </radialGradient>
        <radialGradient id="saladTone" cx="50%" cy="50%" r="50%">
          <stop offset="0" stop-color="#e0a24c"/>
          <stop offset="1" stop-color="#c87a3a"/>
        </radialGradient>
      </defs>

      <g role="img" aria-label="Overhead photo of Vietnamese dishes with herbs and chillies on a dark table">
        <path d="M0 0 H640 C625 60 660 110 560 200 L560 420 C470 470 420 540 330 555 C220 570 100 560 0 548 Z" fill="url(#photoTone)"/>
        <circle cx="335" cy="222" r="140" fill="#fff"/>
        <circle cx="335" cy="222" r="122" fill="url(#soupTone)"/>
        <circle cx="60" cy="70" r="130" fill="#fff"/>
        <circle cx="60" cy="70" r="112" fill="#9a6a45"/>
        <circle cx="0" cy="320" r="100" fill="#fff"/>
        <circle cx="0" cy="320" r="85" fill="#d6a05a"/>
        <rect x="340" y="0" width="230" height="95" rx="12" fill="#f2eee8"/>
      </g>

      <path d="M0 548 C100 560 220 570 330 555 C400 545 440 520 480 500 L470 540 C420 570 330 590 200 590 L0 580 Z" fill="var(--orange)"/>

      <circle cx="190" cy="532" r="140" fill="var(--orange)"/>
      <circle cx="190" cy="532" r="128" fill="#fff"/>
      <g role="img" aria-label="Bowl of rice noodles with shredded chicken and spring onion">
        <circle cx="190" cy="532" r="112" fill="url(#noodleTone)"/>
      </g>

      <circle cx="689" cy="217" r="150" fill="var(--orange)"/>
      <circle cx="689" cy="217" r="138" fill="#fff"/>
      <g role="img" aria-label="Bowl of crispy chicken noodle salad with cucumber and carrot">
        <circle cx="689" cy="217" r="122" fill="url(#saladTone)"/>
      </g>
      <line x1="575" y1="10" x2="600" y2="360" stroke="#111" stroke-width="5"/>
      <line x1="585" y1="10" x2="610" y2="360" stroke="#111" stroke-width="5"/>

      <circle cx="534" cy="497" r="130" fill="var(--orange)"/>
      <circle cx="534" cy="497" r="120" fill="var(--black)"/>

      <path d="M0 1140 C150 1175 300 1180 440 1158 C560 1138 640 1135 700 1150 C780 1172 830 1180 890 1168 V1258 H0 Z" fill="var(--white)"/>
      <path d="M0 1158 C150 1190 300 1195 440 1172 C560 1152 640 1150 700 1165 C780 1186 830 1194 890 1182 V1258 H0 Z" fill="var(--orange)"/>

      <circle cx="739" cy="1160" r="122" fill="#fff"/>
      <g role="img" aria-label="Bowl of fried tofu with bean sprouts, cucumber and herbs">
        <circle cx="739" cy="1160" r="106" fill="#d88a44"/>
      </g>
    </svg>

    <h1 class="badge-title"><span class="kicker">Catering</span><span class="main">Menu</span></h1>

    <section class="menu-block pack-one">
      <h2 class="pack-label">Pack 1:</h2>
      <h3 class="section-head">$15 per person (min 10 people) this includes:</h3>
      <ul class="items">
        <li>10 x Noodle Salads / Pho (All options included)</li>
        <li>10 x Fresh Ricepaper Rolls</li>
        <li>10 x Spring Rolls</li>
      </ul>
    </section>

    <section class="menu-block pack-two">
      <h2 class="pack-label">Pack 1:</h2>
      <h3 class="section-head">$20 per person (min 10 people) this includes:</h3>
      <ul class="items">
        <li>10 x Rice (All options included)</li>
        <li>10 x Spring Rolls</li>
      </ul>
    </section>

    <section class="menu-block fried-rice">
      <h3 class="section-head">Fried rice (all options included)</h3>
      <ul class="items">
        <li>$50 per tray. Serve 5-7 people.</li>
      </ul>
    </section>

    <section class="menu-block spring-rolls">
      <h3 class="section-head">Spring rolls (seafood / vegetarian)</h3>
      <ul class="items">
        <li>20 Rolls = <strong>$30</strong></li>
        <li>30 Rolls = <strong>$45</strong></li>
        <li>40 Rolls = <strong>$60</strong></li>
        <li>50 Rolls = <strong>$75</strong></li>
      </ul>
    </section>

    <section class="menu-block ricepaper-rolls">
      <h3 class="section-head">Fresh ricepaper rolls</h3>
      <ul class="items">
        <li>20 Rolls = <strong>$50</strong></li>
        <li>30 Rolls = <strong>$75</strong></li>
        <li>40 Rolls = <strong>$100</strong></li>
        <li>50 Rolls = <strong>$125</strong></li>
      </ul>
    </section>

    <p class="call-line">
      <span>Call today:</span>
      <svg viewBox="0 0 36 36" aria-hidden="true">
        <rect width="36" height="36" rx="6" fill="#0d0d0d"/>
        <path d="M12 8 C10 9 8 11 9 15 C11 22 15 26 21 28 C25 29 27 27 28 25 L24 21 L21 23 C18 21 15 18 13 15 L15 12 Z" fill="#ec942f"/>
      </svg>
      <span>+01 555 0142 77</span>
    </p>
  </div>
</div>
</body>
</html>
```